Startup Eyewear Store need Website

We are launching a new eyewear store. It's fun retro colors with bold wood tones. I will upload our logo to give you an idea of some fun colors. The site will need a cart and the ability to show multiple view of different eyewear frames. It will need standard buttons such as Contact Us, About Us, Blog, Social Media Feed, and New Releases, . The company will also have a Membership function and we need to be able to show that we can ship multiple frames have customers try them on and select which ones they want. We will need it responsive and all coding done.

Industry/Entity Type

Eyewear

Coding

Coded - Design and coding required

Number of Pages Required

1 page

Colors
f78f20

Requirements
Must have
• Clean Fund and Vintage Retro with some bright oranges.

```html
<!DOCTYPE html>
<html lang="en">
<head>
<meta charset="utf-8">
<title>Frameloft — Eyewear Store</title>
<link href="https://fonts.googleapis.com/css2?family=Raleway:ital,wght@0,400;0,500;0,600;0,700;0,800;1,400;1,500&display=swap" rel="stylesheet">
<style>
:root{
  --orange:#f78f20;
  --orange-dark:#e07a0c;
  --ink:#2b2b2b;
  --text:#444;
  --muted:#8a8a8a;
  --white:#fff;
  --panel:#e6e6e6;
  --footer:#ebebeb;
  --star-off:#9a9a9a;
}
*{box-sizing:border-box;margin:0;padding:0}
html,body{width:1200px;height:2862px;overflow:hidden}
body{position:relative;background:var(--white);font-family:"Raleway",Arial,sans-serif;color:var(--text)}
.abs{position:absolute}

/* hero + header */
.hero{left:0;top:0;width:1200px;height:687px;background:linear-gradient(100deg,#3b2a17 0%,#6b4d26 30%,#8a6a3a 50%,#4a3524 75%,#2c2219 100%)}
.header{left:0;top:0;width:1200px;height:158px;background:rgba(25,20,15,.72)}
.topbar{left:582px;top:0;width:563px;height:34px;background:var(--orange);clip-path:polygon(14px 0,100% 0,100% 100%,0 100%)}
.social{left:612px;top:5px;display:flex;gap:8px}
.social span{width:24px;height:24px;border:2px solid var(--white);border-radius:50%}
.toplinks{left:790px;top:9px;display:flex;gap:0;font-size:12.5px;color:var(--white)}
.toplinks span{padding:0 16px;border-left:1px solid rgba(255,255,255,.7)}
.toplinks span:first-child{border-left:none}
.logo{left:95px;top:19px;width:240px;height:124px}
.logo .dot{left:60px;top:0;width:58px;height:58px;border-radius:50%;background:#ee3d2a}
.logo .name{left:0;top:80px;font-size:34px;font-weight:500;color:#ee5a2a;letter-spacing:-.5px}
.search{left:954px;top:61px;width:185px;height:29px;border:1.5px solid var(--white);color:var(--white);font-size:12px;padding:6px 8px}
.search svg{position:absolute;right:7px;top:5px}
.nav{left:468px;top:118px;display:flex;font-size:18.5px;color:var(--white);font-weight:500}
.nav a{color:inherit;text-decoration:none;margin-right:31px}
.caption{left:61px;top:305px;width:464px;height:197px;background:rgba(35,30,25,.72)}
.caption h1{position:absolute;left:34px;top:22px;font-size:38px;font-weight:600;color:var(--white);letter-spacing:-.3px}
.caption p{position:absolute;left:34px;top:74px;font-size:16px;color:var(--white)}
.btn{position:absolute;left:34px;top:132px;width:170px;height:40px;background:var(--orange);color:var(--white);font-size:14px;font-weight:600;line-height:40px;text-align:center}
.arrow{top:402px}

/* categories */
.cat{top:719px;width:340px;height:191px;overflow:hidden}
.cat-women{left:61px;background:linear-gradient(120deg,#2a2a2a,#5a5550 55%,#1e1e1e)}
.cat-men{left:431px;background:linear-gradient(120deg,#4d463e,#8a7a66 50%,#3a342e)}
.cat-kids{left:801px;background:linear-gradient(180deg,#a8c4d8 0%,#c9b590 40%,#6f9a3c 80%,#4c7a26)}
.cat-women .frame{position:absolute;left:8px;top:80px;width:110px;height:104px;border-left:2px solid var(--white);border-top:2px solid var(--white)}
.cat-women .label{position:absolute;left:20px;top:128px;color:var(--white);font-size:22px;font-weight:500;line-height:1}
.cat-women .label small{display:block;font-size:16px;font-weight:500;margin-top:3px}
.cat-men .frame{position:absolute;left:10px;top:10px;width:320px;height:171px;border:2px solid var(--white)}
.cat-men .label{position:absolute;left:0;width:340px;top:110px;text-align:center;color:var(--white);font-size:31px;font-weight:700}
.cat-men .label small{display:block;font-size:19px;font-weight:500;letter-spacing:6px;margin-top:0}
.cat-kids .tag{position:absolute;left:70px;top:132px;width:204px;height:42px;background:#1c1c1c;border:2px solid var(--white);color:var(--white);font-size:14px;font-weight:700;text-align:center;line-height:38px}

/* featured */
.section-sub{left:0;width:1200px;top:962px;text-align:center;font-size:14px;color:var(--ink)}
.section-title{left:0;width:1200px;top:982px;text-align:center;font-size:28px;color:var(--orange);font-weight:500}
.product{width:256px;text-align:center}
.product .shot{height:296px;position:relative}
.product .shot i{position:absolute;left:18px;top:100px;width:220px;height:96px;border-radius:44px}
.product.active .shot{border:2px solid var(--orange)}
.product h3{font-size:14px;font-weight:500;color:var(--ink);margin-top:30px}
.stars{font-size:15px;letter-spacing:1px;margin-top:5px;color:var(--star-off)}
.stars b{color:var(--orange);font-weight:400}
.price{font-size:15px;margin-top:4px;font-weight:600}
.price s{color:var(--muted);font-weight:500;margin-right:12px}
.price span{color:var(--orange)}
.t-tort{background:radial-gradient(ellipse,#8a4a1c 0%,#c27a36 50%,rgba(255,255,255,0) 72%)}
.t-dark{background:radial-gradient(ellipse,#34415a 0%,#6f6a64 50%,rgba(255,255,255,0) 72%)}
.t-teal{background:radial-gradient(ellipse,#3fc9c2 0%,#9ad9c8 50%,rgba(255,255,255,0) 72%)}
.t-wood{background:radial-gradient(ellipse,#a86a30 0%,#d19a5c 50%,rgba(255,255,255,0) 72%)}

/* promo */
.promo{left:0;top:1956px;width:1200px;height:376px;background:linear-gradient(100deg,#0f0f10 0%,#2a2622 40%,#3a322a 60%,#141414 100%)}
.promo .line{position:absolute;left:366px;width:470px;height:1px;background:rgba(255,255,255,.8)}
.promo .kicker{position:absolute;left:0;width:1200px;top:62px;text-align:center;color:var(--white);font-size:34px;font-style:italic;letter-spacing:2px}
.promo h2{position:absolute;left:0;width:1200px;top:138px;text-align:center;color:var(--white);font-size:55px;font-weight:800;letter-spacing:1px}
.promo .offer{position:absolute;left:0;width:1200px;top:228px;text-align:center;color:var(--white);font-size:24px}
.promo .fine{position:absolute;left:0;width:1200px;top:283px;text-align:center;color:var(--white);font-size:11px}

/* perks */
.perk{top:2373px;width:346px;height:94px;background:var(--panel)}
.perk svg{position:absolute;left:24px;top:23px}
.perk h4{position:absolute;left:110px;top:25px;font-size:25px;font-weight:500;color:var(--ink)}
.perk p{position:absolute;left:110px;top:57px;font-size:11.5px;color:var(--ink)}

/* footer */
.footer{left:0;top:2503px;width:1200px;height:321px;background:var(--footer)}
.col{top:2592px;font-size:13px;color:var(--ink)}
.col h5{font-size:18px;font-weight:600;color:var(--ink);margin-bottom:24px;letter-spacing:.3px}
.info li{list-style:none;display:flex;gap:12px;margin-bottom:20px;line-height:1.5;width:250px}
.info svg{flex:none;margin-top:2px}
.account li{margin-left:18px;margin-bottom:12px}
.badges{display:flex;gap:8px;margin-bottom:12px}
.badges span{width:40px;height:22px;border-radius:3px;background:#c9c9c9}
.col h6{font-size:13px;font-weight:700;margin:6px 0 14px}
.newsletter p{width:270px;line-height:1.6;margin-bottom:12px}
.news-form{display:flex}
.news-form span{width:197px;height:33px;background:var(--white);border:1px solid #ccc;font-size:11px;padding:9px 8px;color:#666}
.news-form b{width:53px;height:33px;background:var(--orange);display:flex;align-items:center;justify-content:center}
.foot-social{display:flex;gap:18px;margin-top:20px}
.foot-social span{width:12px;height:12px;border-radius:50%;background:#9a9a9a}
.bottombar{left:0;top:2824px;width:1200px;height:38px;background:var(--orange);color:var(--white);font-size:11.5px}
.bottombar .copy{position:absolute;left:59px;top:12px}
.bottombar .links{position:absolute;right:60px;top:12px;display:flex;gap:22px}
</style>
</head>
<body>

<div class="abs hero" role="img" aria-label="Photo of a woman in a plaid shirt adjusting yellow retro sunglasses"></div>
<div class="abs header"></div>
<div class="abs topbar"></div>
<div class="abs social"><span></span><span></span><span></span><span></span></div>
<div class="abs toplinks"><span>My Account</span><span>Wish List (0)</span><span>Shopping Cart</span><span>Checkout</span></div>

<div class="abs logo">
  <div class="abs dot"></div>
  <div class="abs name">Frameloft</div>
</div>

<div class="abs search">Search
  <svg width="18" height="18" viewBox="0 0 18 18" fill="none" stroke="#fff" stroke-width="2"><circle cx="7.5" cy="7.5" r="5.5"/><path d="M11.5 11.5l5 5"/></svg>
</div>

<nav class="abs nav"><a>Home</a><a>About Us</a><a>Blogs</a><a>New Releases</a><a>Membership</a><a>Contact Us</a></nav>

<div class="abs caption">
  <h1>Designed For Dreamers</h1>
  <p>Discover Your Perfect Pair</p>
  <span class="btn">View All Collection</span>
</div>
<svg class="abs arrow" style="left:18px" width="24" height="44" viewBox="0 0 24 44" fill="none" stroke="#fff" stroke-width="3"><path d="M20 4L5 22l15 18"/></svg>
<svg class="abs arrow" style="left:1158px" width="24" height="44" viewBox="0 0 24 44" fill="none" stroke="#fff" stroke-width="3"><path d="M4 4l15 18L4 40"/></svg>

<div class="abs cat cat-women" role="img" aria-label="Photo of a woman in oversized round glasses">
  <div class="frame"></div>
  <div class="label">WOMEN'S<small>Collection</small></div>
</div>
<div class="abs cat cat-men" role="img" aria-label="Photo of a bearded man holding up his glasses">
  <div class="frame"></div>
  <div class="label">FASHION<small>CRAZY MEN</small></div>
</div>
<div class="abs cat cat-kids" role="img" aria-label="Photo of three children wearing colourful sunglasses on grass">
  <div class="tag">NEW FUNKY STYLE 2016</div>
</div>

<div class="abs section-sub">We Recommed</div>
<div class="abs section-title">Featured Products</div>

<div class="abs product" style="left:59px;top:1068px"><div class="shot" role="img" aria-label="Tortoiseshell round sunglasses"><i class="t-tort"></i></div><h3>Luma Classique Eyeglasses</h3><div class="stars"><b>★★★</b>★★</div><div class="price"><s>$30.00</s><span>$25.00</span></div></div>
<div class="abs product" style="left:336px;top:1068px"><div class="shot" role="img" aria-label="Cat-eye sunglasses with gradient blue lenses"><i class="t-dark"></i></div><h3>Orro Vento Eyeglasses</h3><div class="stars"><b>★★★</b>★★</div><div class="price"><s>$26.00</s><span>$20.00</span></div></div>
<div class="abs product active" style="left:611px;top:1068px"><div class="shot" role="img" aria-label="Teal and tortoise round sunglasses"><i class="t-teal"></i></div><h3 style="margin-top:28px">Luma Classique Eyeglasses</h3><div class="stars"><b>★★</b>★★★</div><div class="price"><s>$26.00</s><span>$15.00</span></div></div>
<div class="abs product" style="left:887px;top:1068px"><div class="shot" role="img" aria-label="Wood grain round sunglasses"><i class="t-wood"></i></div><h3>Orro Vento Eyeglasses</h3><div class="stars"><b>★★★★</b>★</div><div class="price"><s>$26.00</s><span>$18.00</span></div></div>

<div class="abs product" style="left:59px;top:1500px"><div class="shot" role="img" aria-label="Wood grain round sunglasses"><i class="t-wood"></i></div><h3>Luma Classique Eyeglasses</h3><div class="stars"><b>★★★</b>★★</div><div class="price"><s>$30.00</s><span>$25.00</span></div></div>
<div class="abs product" style="left:336px;top:1500px"><div class="shot" role="img" aria-label="Teal and tortoise round sunglasses"><i class="t-teal"></i></div><h3>Orro Vento Eyeglasses</h3><div class="stars"><b>★★★</b>★★</div><div class="price"><s>$26.00</s><span>$20.00</span></div></div>
<div class="abs product" style="left:611px;top:1500px"><div class="shot" role="img" aria-label="Cat-eye sunglasses with gradient blue lenses"><i class="t-dark"></i></div><h3>Luma Classique Eyeglasses</h3><div class="stars"><b>★★</b>★★★</div><div class="price"><s>$26.00</s><span>$15.00</span></div></div>
<div class="abs product" style="left:887px;top:1500px"><div class="shot" role="img" aria-label="Tortoiseshell round sunglasses"><i class="t-tort"></i></div><h3>Orro Vento Eyeglasses</h3><div class="stars"><b>★★★★</b>★</div><div class="price"><s>$26.00</s><span>$18.00</span></div></div>

<section class="abs promo" role="img" aria-label="Dark photo of a woman lying down wearing sunglasses">
  <div class="kicker">NEW COLLECTION 2016</div>
  <div class="line" style="top:112px"></div>
  <h2>FREE SHIPPING</h2>
  <div class="line" style="top:211px"></div>
  <div class="offer">OF EVERY ODER OVER $250.00</div>
  <div class="fine">THIS OFFER IS VAILD ON ALL OUR STORE ITEMS</div>
</section>

<div class="abs perk" style="left:61px">
  <svg width="56" height="48" viewBox="0 0 56 48" fill="none" stroke="#f78f20" stroke-width="2.5" stroke-linejoin="round"><path d="M6 30l14-2 12-14 6 0-6 14 12-1 6-6h4l-3 10 3 10h-4l-6-6-12-1 6 14h-6L20 32 6 30z"/></svg>
  <h4>Free Shipping</h4><p>On All Order of USD 250.00</p>
</div>
<div class="abs perk" style="left:427px">
  <svg width="52" height="48" viewBox="0 0 52 48" fill="#f78f20"><rect x="6" y="18" width="40" height="26" rx="2"/><rect x="3" y="10" width="46" height="10" rx="2"/><rect x="23" y="10" width="6" height="34" fill="#e6e6e6"/><path d="M26 10c-4-8-14-9-13-3 1 4 8 3 13 3zM26 10c4-8 14-9 13-3-1 4-8 3-13 3z"/></svg>
  <h4>Special Gift Cards</h4><p>Give The Perfect Gift</p>
</div>
<div class="abs perk" style="left:794px">
  <svg width="50" height="50" viewBox="0 0 50 50" fill="none" stroke="#f78f20" stroke-width="3"><path d="M40 14A18 18 0 1 0 43 28"/><path d="M42 4v11H31" stroke-linejoin="round"/></svg>
  <h4>100% Money Back</h4><p>Hourse: 123 456 7890</p>
</div>

<footer class="abs footer"></footer>
<div class="abs col info" style="left:59px">
  <h5>STORE INFORMATION</h5>
  <ul>
    <li><svg width="16" height="16" viewBox="0 0 16 16" fill="none" stroke="#666" stroke-width="1.4"><path d="M2 8l6-6 6 6M4 7v7h8V7"/></svg><span>48 Maple Hollow Rd, Brookside District, Westford</span></li>
    <li><svg width="16" height="16" viewBox="0 0 16 16" fill="none" stroke="#666" stroke-width="1.4"><rect x="4" y="1" width="8" height="14" rx="1.5"/><path d="M7 12h2"/></svg><span>+1 555 014 2290</span></li>
    <li><svg width="16" height="16" viewBox="0 0 16 16" fill="none" stroke="#666" stroke-width="1.4"><rect x="1" y="3" width="14" height="10"/><path d="M1 3l7 6 7-6"/></svg><span>hello@frameloft.shop</span></li>
  </ul>
</div>
<div class="abs col account" style="left:351px">
  <h5>MY ACCOUNT</h5>
  <ul><li>My orders</li><li>My credit slips</li><li>My addresses</li><li>My personal info</li><li>My vouchers</li></ul>
</div>
<div class="abs col" style="left:578px">
  <h5>PAYMENT METHODS</h5>
  <div class="badges"><span></span><span></span><span></span><span></span></div>
  <h6>SHIPPING PARTNER</h6>
  <div class="badges"><span></span><span></span><span></span><span></span></div>
  <div class="badges"><span></span><span></span><span></span></div>
</div>
<div class="abs col newsletter" style="left:881px">
  <h5>NEWSLETTER !</h5>
  <p>Sign up for our newsletter and get 15% off your next order.</p>
  <div class="news-form"><span>Enter your email here*</span><b><svg width="20" height="12" viewBox="0 0 20 12" fill="none" stroke="#fff" stroke-width="2"><path d="M1 6h16M12 1l5 5-5 5"/></svg></b></div>
  <div class="foot-social"><span></span><span></span><span></span><span></span><span></span></div>
</div>

<div class="abs bottombar">
  <div class="copy">© 2016 Copyright Frameloft.&nbsp; All Right Reserved.</div>
  <div class="links"><span>Privacy &amp; Cookies</span><span>Terms &amp; Conditions</span><span>Accessibility</span><span>Store Directory</span><span>About Us</span></div>
</div>

</body>
</html>
```